Modern 6 page design, business card, and a banner

I need a website design for my CFO service. The service uses proprietary tech, so it needs to be modern. I also need business card and banner design to match the site.
The banner size is 33.75 X 79.25.
I'm open to colors and styles.

Target Market(s)

Startups

Coding

Coded - Design and coding required

Number of Pages Required

5+ page

```html
<!DOCTYPE html>
<html lang="en">
<head>
<meta charset="utf-8">
<title>Tallo – Strategic Financial Planner</title>
<link href="https://fonts.googleapis.com/css2?family=Oswald:wght@500;600&family=Questrial&family=Raleway:wght@300;400;500&display=swap" rel="stylesheet">
<style>
:root{
  --navy:#2f2a52;
  --navy-deep:#27234a;
  --pink:#d8908f;
  --pink-soft:#e7b2b0;
  --accent:#e48b82;
  --mist:#f4f4f8;
  --ink:#3b3b4a;
  --footer:#434343;
  --white:#ffffff;
}
*{box-sizing:border-box;margin:0;padding:0}
html,body{width:1200px;height:3429px;overflow:hidden}
body{position:relative;background:var(--white);font-family:'Raleway',sans-serif;color:var(--ink)}
.abs{position:absolute}

/* hero */
.hero{position:absolute;left:0;top:0;width:1200px;height:690px}
.hero-bg{position:absolute;inset:0}
.brand{position:absolute;left:110px;top:18px;color:var(--white)}
.brand-name{font-family:'Questrial',sans-serif;font-size:60px;line-height:64px;font-weight:400;letter-spacing:1px}
.brand-tag{font-family:'Questrial',sans-serif;font-size:11px;color:var(--accent);font-weight:600;margin-top:4px}
.top-contact{position:absolute;right:112px;top:20px;display:flex;gap:22px;color:var(--white);font-family:'Questrial',sans-serif;font-size:18px}
.top-contact span{display:flex;align-items:center;gap:10px}
.ring-icon{width:36px;height:36px;border:2px solid var(--white);border-radius:50%;display:flex;align-items:center;justify-content:center}
.nav{position:absolute;right:112px;top:74px;display:flex;gap:20px;font-family:'Questrial',sans-serif;font-size:16px;color:var(--white)}
.nav a{color:inherit;text-decoration:none;padding:8px 16px}
.nav a.active{background:rgba(255,255,255,.18);border-radius:20px;padding:8px 16px}
.nav a:not(.active){padding:8px 0}
.hero-title{position:absolute;left:110px;top:226px;font-family:'Questrial',sans-serif;font-size:40px;color:var(--white);font-weight:600}
.hero-lead{position:absolute;left:110px;top:300px;width:520px;font-family:'Questrial',sans-serif;font-size:20px;line-height:31px;color:var(--white)}
.btn{display:inline-block;font-family:'Questrial',sans-serif;font-size:17px;border-radius:26px;padding:13px 19px}
.btn-outline{position:absolute;left:110px;top:400px;border:2px solid var(--white);color:var(--white)}
.btn-navy{background:var(--navy);color:var(--white)}
.device{position:absolute;border:3px solid #e4e4ea;background:#fafafc;border-radius:40px}
.device .screen{position:absolute;left:14px;right:14px;top:62px;bottom:70px}

/* headings */
.sec-title{position:absolute;left:0;width:1200px;text-align:center;font-family:'Oswald',sans-serif;font-size:38px;font-weight:600;color:var(--navy);letter-spacing:.5px}
.sec-title em{font-style:normal;color:var(--pink)}
.rule{position:absolute;height:3px;width:76px;background:var(--navy)}

.about-text{position:absolute;left:110px;width:980px;text-align:center;font-size:15px;line-height:26px;font-weight:400}
.about-text p+p{margin-top:17px}

/* how it works */
.how{position:absolute;left:0;top:1080px;width:1200px;height:596px;background:var(--mist)}
.step{position:absolute;width:140px;height:140px;border-radius:50%;border:3px dashed var(--pink);display:flex;align-items:center;justify-content:center}
.step-core{width:116px;height:116px;border-radius:50%;background:var(--pink);color:var(--white);display:flex;flex-direction:column;align-items:center;justify-content:center;font-family:'Questrial',sans-serif;font-size:15px;line-height:21px;text-align:center}
.step-shadow{position:absolute;width:40px;height:3px;border-radius:2px;background:#cfcfd6}
.step-big{position:absolute;left:809px;top:1315px;width:280px;height:280px;border-radius:50%;border:5px dashed var(--navy);display:flex;align-items:center;justify-content:center}
.step-big .step-core{width:246px;height:246px;background:var(--navy);font-size:14px;line-height:20px}
.step-big h3{font-family:'Questrial',sans-serif;font-size:21px;font-weight:600;margin:10px 0 10px}

/* feature blocks */
.feat-title{position:absolute;font-family:'Oswald',sans-serif;font-size:29px;font-weight:600;color:var(--navy);letter-spacing:.3px}
.feat-title em{font-style:normal;color:var(--pink)}
.feat-text{position:absolute;font-size:14.5px;line-height:26px}
.feat-text p+p{margin-top:16px}

/* footer */
.footer{position:absolute;left:0;top:2965px;width:1200px;height:464px;background:var(--footer);color:var(--white)}
.footer h2{position:absolute;left:110px;top:80px;font-family:'Oswald',sans-serif;font-size:32px;font-weight:500}
.field{position:absolute;border:2px solid var(--white);border-radius:24px;font-family:'Questrial',sans-serif;font-size:16px;padding:12px 18px}
.btn-white{position:absolute;left:112px;top:360px;background:var(--white);color:var(--ink)}
.foot-brand{position:absolute;right:112px;top:66px;text-align:right}
.foot-brand .brand-name{font-size:100px;line-height:110px}
.foot-brand .brand-tag{color:var(--white);font-size:16px;margin-top:12px}
.foot-contact{position:absolute;right:112px;top:288px;display:flex;gap:18px;font-family:'Questrial',sans-serif;font-size:16px}
.foot-contact span{display:flex;align-items:center;gap:10px}
.foot-line{position:absolute;left:714px;top:363px;width:374px;height:2px;background:var(--white)}
.copy{position:absolute;right:112px;top:393px;font-family:'Questrial',sans-serif;font-size:15px}
</style>
</head>
<body>

<!-- HERO -->
<header class="hero">
  <svg class="hero-bg" width="1200" height="690" viewBox="0 0 1200 690">
    <defs><linearGradient id="heroG" x1="0" y1="0" x2="1" y2="1"><stop offset="0" stop-color="#34305a"/><stop offset="1" stop-color="#2a2650"/></linearGradient></defs>
    <path d="M0 0H1200V520C1090 525 1020 560 900 590C760 625 620 560 430 575C260 590 140 670 0 670Z" fill="url(#heroG)"/>
  </svg>
  <div class="brand"><div class="brand-name">Tallo</div><div class="brand-tag">Strategic Financial Planner</div></div>
  <div class="top-contact">
    <span><i class="ring-icon"><svg width="16" height="12" viewBox="0 0 16 12" fill="none" stroke="#fff" stroke-width="1.6"><rect x="1" y="1" width="14" height="10" rx="1.5"/><path d="M1 2l7 5 7-5"/></svg></i>info@tallo.com</span>
    <span><i class="ring-icon"><svg width="16" height="16" viewBox="0 0 24 24" fill="#fff"><path d="M6.6 10.8a15 15 0 006.6 6.6l2.2-2.2a1 1 0 011-.25 11.4 11.4 0 003.6.6 1 1 0 011 1V20a1 1 0 01-1 1A17 17 0 013 4a1 1 0 011-1h3.5a1 1 0 011 1c0 1.25.2 2.45.6 3.6a1 1 0 01-.25 1z"/></svg></i>+123 555 0190</span>
  </div>
  <nav class="nav"><a class="active">HOME</a><a>ABOUT US</a><a>HOW IT WORKS</a><a>WHY TALLO</a><a>BLOG</a><a>CONTACT US</a></nav>
  <h1 class="hero-title">Strategic Financial Planner</h1>
  <p class="hero-lead">Tallo combines hands-on financial planning services with real-time mobile monitoring.</p>
  <span class="btn btn-outline">Read More</span>
  <div class="device" style="left:817px;top:172px;width:272px;height:512px">
    <div class="screen" role="img" aria-label="Illustration of financial charts, gears and a calculator" style="top:64px;bottom:70px;background:linear-gradient(160deg,#3a3fb0,#2b2f95)"></div>
  </div>
</header>

<!-- ABOUT -->
<h2 class="sec-title" style="top:752px">ABOUT <em>TALLO</em></h2>
<div class="rule" style="left:562px;top:814px"></div>
<div class="about-text" style="top:858px">
  <p>Small businesses can visualize their finances, have a plan they trust and monitor progress daily. No more waiting for the latest monthly or quarterly report from your accountant. No more late nights digging through spreadsheets to figure out where you really stand. No more wondering if you're prepared for the future.</p>
  <p>Tallo delivers a clear financial plan tailored to your goals, an easy mobile dashboard to track progress on a daily basis and all the professional advice and support you need along the way.</p>
</div>

<!-- HOW IT WORKS -->
<section class="how"></section>
<h2 class="sec-title" style="top:1146px">HOW IT <em>WORKS</em></h2>
<div class="rule" style="left:562px;top:1209px"></div>
<svg class="abs" style="left:0;top:1300px" width="1200" height="180" viewBox="0 0 1200 180" fill="none" stroke="#c9c9d2" stroke-width="1.5" stroke-dasharray="6 6">
  <path d="M0 30C60 50 90 80 120 100M240 110C270 110 280 80 300 70M420 70C440 70 450 75 470 70M600 80C620 90 640 110 655 115M1090 105C1130 80 1170 60 1200 45"/>
</svg>
<div class="step" style="left:111px;top:1324px"><div class="step-core"><svg width="32" height="30" viewBox="0 0 32 30" fill="none" stroke="#fff" stroke-width="1.6"><rect x="2" y="4" width="14" height="22"/><path d="M20 26V4l10 22z"/></svg><span style="margin-top:6px">DEVELOP<br>PLAN</span></div></div>
<div class="step-shadow" style="left:161px;top:1480px"></div>
<div class="step" style="left:291px;top:1314px"><div class="step-core"><svg width="30" height="30" viewBox="0 0 30 30" fill="none" stroke="#fff" stroke-width="1.6"><rect x="3" y="3" width="18" height="22"/><circle cx="20" cy="20" r="6"/></svg><span style="margin-top:6px">CLEAN<br>DATA</span></div></div>
<div class="step-shadow" style="left:341px;top:1472px"></div>
<div class="step" style="left:471px;top:1304px"><div class="step-core"><svg width="32" height="30" viewBox="0 0 32 30" fill="none" stroke="#fff" stroke-width="1.6"><rect x="8" y="2" width="18" height="24"/><path d="M3 10v18h20M12 8h10M12 13h10M12 18h10"/></svg><span style="margin-top:6px">VISUAL<br>FINANCES</span></div></div>
<div class="step-shadow" style="left:521px;top:1464px"></div>
<div class="step" style="left:651px;top:1336px"><div class="step-core"><svg width="34" height="30" viewBox="0 0 34 30" fill="none" stroke="#fff" stroke-width="1.6"><rect x="2" y="2" width="30" height="20" rx="1"/><path d="M12 28h10M17 22v6M2 16h30"/></svg><span style="margin-top:6px">MONITOR<br>DAILY</span></div></div>
<div class="step-shadow" style="left:701px;top:1498px"></div>
<div class="step-big"><div class="step-core">
  <svg width="56" height="54" viewBox="0 0 56 54" fill="none" stroke="#fff" stroke-width="2.4"><rect x="3" y="8" width="50" height="43" rx="2"/><path d="M3 18h50M14 3v10M28 3v10M42 3v10"/><path d="M12 27h6M25 27h6M38 27h6M12 35h6M25 35h6M38 35h6M12 43h6M25 43h6M38 43h6"/></svg>
  <h3>ADVISE MONTHLY</h3>
  <span>our financial experts provide<br>support and help respond as<br>your business grows</span>
</div></div>

<!-- VISUALIZE -->
<svg class="abs" style="left:0;top:1676px" width="1200" height="600" viewBox="0 0 1200 600">
  <path d="M840 130C950 70 1080 40 1200 0V520C1130 560 1050 590 960 560C880 530 850 400 840 300Z" fill="var(--pink)"/>
</svg>
<h2 class="feat-title" style="left:110px;top:1834px">VISUALIZE YOUR FINANCES IN REAL TIME.</h2>
<div class="rule" style="left:110px;top:1890px;width:100px"></div>
<div class="feat-text" style="left:110px;top:1928px;width:516px;text-align:justify">
  <p>Tallo delivers an easy-to-understand dashboard using our own mobile app, customized for your business and your specific plan. Relying on clean data and mirroring your actual financial statements, Tallo lets you see what a CFO sees and always be confident you're looking at real numbers.</p>
  <p>Monitor results daily, understand where you stand versus plan and make better decisions with Tallo Mobile.</p>
</div>
<span class="btn btn-navy abs" style="left:110px;top:2134px">Learn More</span>
<div class="device" style="left:664px;top:1815px;width:150px;height:340px;border-radius:24px"><div class="screen" role="img" aria-label="App screen showing dealer sales gauges" style="left:6px;right:6px;top:38px;bottom:48px;background:linear-gradient(180deg,#2d3a7a,#1f4f9a)"></div></div>
<div class="device" style="left:934px;top:1815px;width:152px;height:340px;border-radius:24px"><div class="screen" role="img" aria-label="App screen showing global sales gauges" style="left:6px;right:6px;top:38px;bottom:48px;background:linear-gradient(180deg,#2d3a7a,#1f4f9a)"></div></div>
<div class="device" style="left:775px;top:1778px;width:204px;height:440px;border-radius:30px"><div class="screen" role="img" aria-label="App screen listing goals with progress bars" style="left:8px;right:8px;top:46px;bottom:56px;background:linear-gradient(180deg,#eef0f4 0,#ffffff 40%,#f3f4f7 100%)"></div></div>

<!-- WHY -->
<svg class="abs" style="left:0;top:2270px" width="1200" height="520" viewBox="0 0 1200 520">
  <path d="M0 0C120 40 260 60 380 70C470 80 530 150 530 260C530 370 470 460 360 480C230 500 120 470 0 440Z" fill="var(--pink)"/>
</svg>
<div class="device" style="left:158px;top:2308px;width:220px;height:490px;border-radius:30px"><div class="screen" role="img" aria-label="App screen showing monthly sales bar chart" style="left:8px;right:8px;top:52px;bottom:58px;background:linear-gradient(180deg,#ffffff,#e7ecf5)"></div></div>
<div class="device" style="left:252px;top:2372px;width:224px;height:466px;border-radius:30px"><div class="screen" role="img" aria-label="App screen showing sales report table" style="left:8px;right:8px;top:50px;bottom:56px;background:linear-gradient(180deg,#ffffff,#f1f2f6)"></div></div>
<h2 class="feat-title" style="left:0;width:1090px;text-align:right;top:2414px;font-size:35px">WHY TALLO <em>VISUAL FINANCE</em></h2>
<div class="rule" style="left:952px;top:2484px;width:138px"></div>
<div class="feat-text" style="left:574px;top:2520px;width:516px;text-align:right">
  <p style="text-align:justify;text-align-last:right">Small businesses shouldn't be forced to choose between the strategic value of traditional financial services and the convenience of modern mobile reporting technology. With Tallo, you have access to decades of financial planning experience and a daily view into real finance reports</p>
  <p>all delivered through a mobile app you can take with you on the road, in the field, on the shop floor or wherever you</p>
</div>
<span class="btn btn-navy abs" style="left:962px;top:2725px">Learn More</span>

<!-- FOOTER -->
<footer class="footer">
  <h2>CONTACT US</h2>
  <div class="rule" style="left:110px;top:133px;width:94px;background:#fff"></div>
  <div class="field" style="left:111px;top:174px;width:247px;height:46px">Name</div>
  <div class="field" style="left:368px;top:174px;width:248px;height:46px">Email</div>
  <div class="field" style="left:111px;top:242px;width:505px;height:98px">Message</div>
  <span class="btn btn-white">Submit Now</span>
  <div class="foot-brand"><div class="brand-name">Tallo</div><div class="brand-tag">Strategic Financial Planner</div></div>
  <div class="foot-contact">
    <span><i class="ring-icon"><svg width="16" height="12" viewBox="0 0 16 12" fill="none" stroke="#fff" stroke-width="1.6"><rect x="1" y="1" width="14" height="10" rx="1.5"/><path d="M1 2l7 5 7-5"/></svg></i>info@tallo.com</span>
    <span><i class="ring-icon"><svg width="16" height="16" viewBox="0 0 24 24" fill="#fff"><path d="M6.6 10.8a15 15 0 006.6 6.6l2.2-2.2a1 1 0 011-.25 11.4 11.4 0 003.6.6 1 1 0 011 1V20a1 1 0 01-1 1A17 17 0 013 4a1 1 0 011-1h3.5a1 1 0 011 1c0 1.25.2 2.45.6 3.6a1 1 0 01-.25 1z"/></svg></i>+123 555 0190</span>
  </div>
  <div class="foot-line"></div>
  <p class="copy">Copyrights @ 2019 Tallo. All Rights Reserved.</p>
</footer>

</body>
</html>
```